Elegant, High End Integrated Wellness Healthcare Practice

We need a brochure designed for an integrated mind-body wellness healthcare practice (www.larchveilclinic.com) . This brochure will be used when we cold call prospects (physicians to refer to our office, and potential consumers to utilize our services). Our practice is geographically located in the middle Tennessee USA region, although we have plans to become an international company as many of our offerings can be accessed anywhere in the world. Ultimately our goal is to have this brochure used as a leave-behind in an effort to introduce our integrated offerings to increase market share. The final product brochure should be both elegant and serious, with clean lines but also convey warmth and trust, as individuals who are coming for our services have usually struggled with their health for a significant amount of time before finding our practice.

The design brief was very specific about providing a high-end science-based 2-page brochure (not flier). Several designs submitted were fliers. The other designs were heavy on yoga or "woo woo" non-science-based looking pictures. This is a flier to appeal to physicians and other healthcare providers. Therefore the design must speak science and evidence-based methods of mind and body wellness care. I would also like to appeal to the other designers I paid extra for their submissions and who have indicated they will "respond in the coming days."

```html
<!DOCTYPE html>
<html lang="en">
<head>
<meta charset="utf-8">
<title>Larchveil Clinic — Brochure Spread</title>
<link rel="stylesheet" href="https://fonts.googleapis.com/css2?family=EB+Garamond:wght@500;700;800&family=Open+Sans:wght@400;600&display=swap">
<style>
  :root {
    --green-deep: #1f3a08;
    --green-mid: #2c4d0e;
    --green-leaf: #6aab35;
    --green-pale: #b9d49e;
    --ink: #1b1b1b;
    --paper: #ffffff;
    --mist: #e9ece6;
  }
  * { box-sizing: border-box; margin: 0; padding: 0; }
  html, body { width: 1200px; height: 797px; overflow: hidden; background: var(--paper); }
  .spread { position: relative; width: 1200px; height: 797px; display: flex; }
  .page { position: relative; width: 600px; height: 797px; overflow: hidden; background: var(--paper); }

  .page-art { position: absolute; inset: 0; }

  .brand { position: absolute; left: 158px; top: 540px; display: flex; align-items: center; gap: 14px; }
  .brand-dot { width: 82px; height: 82px; border-radius: 50%; background: var(--green-mid); }
  .brand-name {
    font-family: "EB Garamond", Georgia, serif; font-weight: 500; font-variant: small-caps;
    color: var(--green-deep); font-size: 36px; line-height: 1.05; letter-spacing: .5px;
  }
  .cover-headline {
    position: absolute; left: 0; right: 0; top: 646px; text-align: center;
    font-family: "EB Garamond", Georgia, serif; font-weight: 800; font-size: 46px; line-height: 54px;
    color: var(--green-deep);
  }
  .cover-headline .accent { color: var(--green-leaf); }

  .inside-title {
    position: absolute; left: 0; right: 0; top: 30px; text-align: center;
    font-family: "EB Garamond", Georgia, serif; font-weight: 800; font-size: 37px; line-height: 42px;
    color: var(--green-deep);
  }
  .inside-title .accent { display: block; color: var(--green-leaf); }

  .service {
    position: absolute; width: 272px; height: 136px; background: var(--paper);
    box-shadow: 0 1px 6px rgba(0,0,0,.16); padding: 18px 18px 0 18px;
    font-family: "Open Sans", Arial, sans-serif;
  }
  .service-title { font-weight: 600; font-size: 13px; line-height: 18px; color: var(--ink); width: 150px; min-height: 36px; }
  .service-number {
    position: absolute; right: 10px; top: 6px; font-weight: 600; font-size: 46px; line-height: 56px;
    color: var(--green-pale);
  }
  .service-text { font-size: 10.2px; line-height: 18px; color: #2a2a2a; margin-top: 2px; }

  .contact {
    position: absolute; left: 0; right: 0; top: 620px; color: var(--paper);
    font-family: "Open Sans", Arial, sans-serif; text-align: center;
  }
  .contact-title { font-family: "EB Garamond", Georgia, serif; font-weight: 700; font-size: 27px; }
  .contact-list { position: relative; height: 110px; }
  .contact-item { position: absolute; top: 30px; width: 190px; margin-left: -95px; font-size: 14px; line-height: 24px; }
  .contact-item svg { display: block; margin: 0 auto 14px; }
</style>
</head>
<body>
<div class="spread">

  <section class="page page-cover">
    <svg class="page-art" width="600" height="797" viewBox="0 0 600 797" aria-hidden="false">
      <defs>
        <linearGradient id="sunsetTones" x1="0" y1="0" x2="0" y2="1">
          <stop offset="0" stop-color="#e7c0a6"/>
          <stop offset=".35" stop-color="#cf9270"/>
          <stop offset=".6" stop-color="#5e4a42"/>
          <stop offset="1" stop-color="#2b2c33"/>
        </linearGradient>
        <radialGradient id="foliageHaze" cx=".5" cy=".5" r=".5">
          <stop offset="0" stop-color="#dfe6d6"/>
          <stop offset="1" stop-color="#ffffff" stop-opacity="0"/>
        </radialGradient>
      </defs>
      <rect x="0" y="0" width="10" height="380" fill="var(--green-leaf)"/>
      <ellipse cx="345" cy="118" rx="395" ry="360" fill="var(--green-deep)"/>
      <ellipse cx="322" cy="104" rx="392" ry="358" fill="var(--green-leaf)"/>
      <ellipse cx="318" cy="96" rx="386" ry="360" fill="url(#sunsetTones)" role="img" aria-label="Photograph: silhouette of a person in a hat against a warm sunset sky"/>
      <ellipse cx="90" cy="600" rx="150" ry="190" fill="url(#foliageHaze)" role="img" aria-label="Faint decorative tree illustration"/>
    </svg>

    <div class="brand">
      <div class="brand-dot"></div>
      <div class="brand-name">Larchveil<br>Clinic</div>
    </div>

    <h1 class="cover-headline">Discover a better way<br>to a <span class="accent">better you</span></h1>
  </section>

  <section class="page page-inside">
    <svg class="page-art" width="600" height="797" viewBox="0 0 600 797">
      <defs>
        <radialGradient id="foliageHazeRight" cx=".5" cy=".5" r=".5">
          <stop offset="0" stop-color="#dfe6d6"/>
          <stop offset="1" stop-color="#ffffff" stop-opacity="0"/>
        </radialGradient>
      </defs>
      <ellipse cx="60" cy="560" rx="130" ry="170" fill="url(#foliageHazeRight)" role="img" aria-label="Faint decorative tree illustration"/>
      <ellipse cx="330" cy="905" rx="385" ry="348" fill="var(--green-leaf)"/>
      <ellipse cx="420" cy="930" rx="470" ry="362" fill="var(--green-deep)"/>
    </svg>

    <h2 class="inside-title">What We Do at<span class="accent">Larchveil Clinic</span></h2>

    <article class="service" style="left:23px; top:152px;">
      <h3 class="service-title">An Integrative Approach</h3>
      <span class="service-number">01</span>
      <p class="service-text">Guided step-by-step by our care team, well embark on an integrative approach to cover more of the issues we face across the lifespan.</p>
    </article>

    <article class="service" style="left:313px; top:152px;">
      <h3 class="service-title">Personalized Care</h3>
      <span class="service-number">02</span>
      <p class="service-text" style="margin-top:-10px">This is no “one-size-fits-all” when it comes to giving yourself the best care. Everyone is biologically unique, and as we age, we have different needs and requirements.</p>
    </article>

    <article class="service" style="left:23px; top:306px;">
      <h3 class="service-title">Innovative Treatments</h3>
      <span class="service-number">03</span>
      <p class="service-text" style="margin-top:-10px">At Larchveil Clinic we provide the best of both worlds...traditional approaches in body &amp; mind health with clinicians who also have advanced training in functional medicine</p>
    </article>

    <article class="service" style="left:313px; top:306px;">
      <h3 class="service-title">Root Cause Resolution</h3>
      <span class="service-number">04</span>
      <p class="service-text">We get to the bottom of WHY you feel sluggish, depressed, anxious, distracted, can’t release stubborn weight, or struggle with brain fog.</p>
    </article>

    <article class="service" style="left:313px; top:462px;">
      <h3 class="service-title">Co-Creating Health</h3>
      <span class="service-number">05</span>
      <p class="service-text" style="margin-top:-10px">Changing your lifestyle may seem daunting, but we also equip you with mindset tools &amp; mentorship to overcome life habits that are an impediment to optimal wellness.</p>
    </article>

    <div class="contact">
      <h2 class="contact-title">Contact Us</h2>
      <div class="contact-list">
        <div class="contact-item" style="left:128px;">
          <svg width="22" height="28" viewBox="0 0 22 28"><path d="M11 0C4.9 0 0 4.8 0 10.8 0 18.5 11 28 11 28s11-9.5 11-17.2C22 4.8 17.1 0 11 0zm0 15a4.3 4.3 0 1 1 0-8.6 4.3 4.3 0 0 1 0 8.6z" fill="#fff"/></svg>
          418 Alder Run Lane,<br>Kestrel Falls, TN, US
        </div>
        <div class="contact-item" style="left:316px;">
          <svg width="24" height="24" viewBox="0 0 24 24"><path d="M6.6 10.8a15.2 15.2 0 0 0 6.6 6.6l2.2-2.2c.3-.3.7-.4 1-.2 1.1.4 2.3.6 3.6.6.6 0 1 .4 1 1V20c0 .6-.4 1-1 1A17 17 0 0 1 3 4c0-.6.4-1 1-1h3.5c.6 0 1 .4 1 1 0 1.3.2 2.5.6 3.6.1.3 0 .7-.2 1l-2.3 2.2z" fill="#fff"/></svg>
          New Patients:<br>(615) 555-0142
        </div>
        <div class="contact-item" style="left:490px;">
          <svg width="24" height="24" viewBox="0 0 24 24"><path d="M6.6 10.8a15.2 15.2 0 0 0 6.6 6.6l2.2-2.2c.3-.3.7-.4 1-.2 1.1.4 2.3.6 3.6.6.6 0 1 .4 1 1V20c0 .6-.4 1-1 1A17 17 0 0 1 3 4c0-.6.4-1 1-1h3.5c.6 0 1 .4 1 1 0 1.3.2 2.5.6 3.6.1.3 0 .7-.2 1l-2.3 2.2z" fill="#fff"/></svg>
          Existing Patients:<br>(615) 555-0187
        </div>
      </div>
    </div>
  </section>

</div>
</body>
</html>
```